Pet store web design

I would like to redesign my current online store (http://brindlecove.example)
I'm looking for a clean, modern design. Any ideas are welcome..

Industry/Entity Type

Pet

Number of Pages Required

3 page

```html
<!DOCTYPE html>
<html lang="en">
<head>
<meta charset="utf-8">
<title>Logo — Pet Store</title>
<link href="https://fonts.googleapis.com/css2?family=Oswald:wght@400;600&family=Open+Sans:wght@400;600;700&family=Lilita+One&display=swap" rel="stylesheet">
<style>
:root{
  --sky-top:#14307a;
  --sky-mid:#2f67c4;
  --sky-low:#8fc3ec;
  --navy:#1b2a5c;
  --navy-deep:#121d44;
  --wood:#7a4a24;
  --wood-dark:#553014;
  --grass:#5ca631;
  --grass-dark:#3c7a1f;
  --orange:#f08a1c;
  --red:#d9472a;
  --blue:#2d7fd0;
  --beige:#f5ece0;
  --beige-line:#e7d8c4;
  --text:#4a4a4a;
  --muted:#9a9a9a;
  --white:#ffffff;
  --purple:#6a3d9a;
  --footer:#2e5a1a;
}
*{box-sizing:border-box;margin:0;padding:0}
html,body{width:783px;height:1200px;overflow:hidden}
body{font-family:"Open Sans",Arial,sans-serif;color:var(--text);background:var(--sky-top)}
.page{position:relative;width:783px;height:1200px;overflow:hidden;
  background:linear-gradient(180deg,var(--sky-top) 0,var(--sky-mid) 500px,var(--sky-low) 980px,#cfe8f7 1040px)}
.abs{position:absolute}

/* top bar */
.top-links{left:48px;top:6px;display:flex;gap:14px;font-size:8px;color:#cfd9f3}
.logo{left:48px;top:34px;font-family:"Oswald",sans-serif;font-size:24px;color:var(--white);font-weight:600}
.doghouse{left:585px;top:6px;width:150px;height:82px;border-radius:6px;
  background:linear-gradient(180deg,#d8452f 0,#d8452f 40%,#4a9ad8 40%,#3f7fc0 100%)}
.ribbon{left:612px;top:82px;width:128px;height:16px;background:var(--navy-deep);color:var(--white);
  font-size:7px;font-weight:700;text-align:center;line-height:16px;border-radius:2px}

/* nav */
.nav{left:40px;top:112px;width:705px;height:36px;background:var(--wood);border-radius:4px;
  border-top:8px solid var(--grass);display:flex;align-items:center;padding:0 14px;box-shadow:0 3px 0 var(--wood-dark)}
.nav ul{list-style:none;display:flex;gap:16px;font-family:"Oswald",sans-serif;font-size:11px;color:var(--white);letter-spacing:.5px}
.nav .dot{width:8px;height:8px;border-radius:50%;background:var(--orange);margin-right:14px}
.search{margin-left:auto;width:150px;height:16px;background:var(--wood-dark);border-radius:2px;
  font-size:7px;color:#d9c2a6;line-height:16px;padding-left:6px;display:flex;justify-content:space-between;padding-right:6px}

/* hero */
.hero-slide{left:40px;top:160px;width:412px;height:118px;border:5px solid var(--navy);border-radius:10px;
  background:linear-gradient(120deg,#6b3a1c,#a8642f 55%,#c8893e)}
.services{left:462px;top:160px;width:283px;height:118px;background:var(--navy);border-radius:10px;padding:8px 12px}
.service{display:flex;align-items:center;justify-content:space-between;height:34px;border-bottom:1px solid #2e3f78}
.service:last-child{border-bottom:0}
.service h3{font-family:"Oswald",sans-serif;font-size:11px;color:var(--white);font-weight:600}
.service p{font-size:6.5px;color:#aab6dc}
.service .go{width:18px;height:18px;border-radius:50%;background:var(--orange);display:flex;align-items:center;justify-content:center}

/* main content */
.main{left:40px;top:284px;width:705px;height:740px;background:var(--white);
  border:10px solid var(--wood);border-radius:14px;box-shadow:0 0 0 3px var(--wood-dark)}
.promo{top:60px;width:320px;height:58px;border-radius:4px;color:var(--white);padding:6px 10px}
.promo h2{font-family:"Lilita One",sans-serif;font-size:17px;font-weight:400;letter-spacing:.5px}
.promo p{font-size:7px}
.promo .btn{display:inline-block;margin-top:4px;font-size:6.5px;font-weight:700;background:rgba(0,0,0,.25);padding:2px 8px;border-radius:2px}
.promo-food{left:8px;background:linear-gradient(90deg,var(--red),var(--orange))}
.promo-school{left:365px;background:linear-gradient(90deg,var(--blue),#5fb0ea)}
.promo .thumb{position:absolute;right:6px;top:6px;width:60px;height:46px;border-radius:3px;background:rgba(255,255,255,.3)}

.col{top:136px;width:160px}
.col h3{font-family:"Oswald",sans-serif;font-size:13px;color:#c9b69c;font-weight:400;margin-bottom:6px}
.col p{font-size:7.5px;line-height:1.55;color:#bfbfbf}
.col .more{display:inline-block;margin-top:14px;font-size:7px;border:1px solid #ddd;padding:2px 6px;color:#999}
.offer{left:500px;top:130px;width:170px;height:120px;background:var(--beige);padding:10px}
.offer h3{font-family:"Oswald",sans-serif;font-size:12px;color:#cdb89b;font-weight:400}
.offer p{font-size:7px;color:#c8b89f;margin-top:6px;line-height:1.5}

.hours{left:14px;top:296px;width:300px;height:106px;background:var(--beige);padding:8px}
.hours table{width:100%;border-collapse:collapse;font-size:7px;color:#b9a88f}
.hours td{border-bottom:1px solid var(--beige-line);padding:3px 4px;height:16px}
.video{left:365px;top:296px;width:305px;height:106px;background:linear-gradient(180deg,#9cb6cf,#6f8597 60%,#3d3f42);border:2px solid #333}

.tabs{left:14px;top:440px;display:flex;gap:18px;font-size:8px;color:#888;border-bottom:1px solid #e2e2e2;width:656px;padding-bottom:4px}
.tabs .on{color:var(--text);font-weight:700}
.products{left:14px;top:466px;width:656px;display:flex;justify-content:space-between}
.product{width:118px;text-align:center;position:relative}
.product .pic{width:70px;height:88px;margin:0 auto;border-radius:3px}
.product h4{font-size:6.5px;font-weight:600;margin-top:10px;color:#555}
.product .stars{font-size:6px;color:#e0b52d;margin-top:2px}
.product .price{font-size:8px;font-weight:700;margin-top:2px;color:#333}
.product .cart{display:inline-block;margin-top:6px;font-size:6px;font-weight:700;color:var(--white);background:var(--blue);padding:3px 7px;border-radius:2px}
.badge{position:absolute;left:4px;top:-6px;width:20px;height:20px;border-radius:50%;background:var(--grass);color:var(--white);font-size:6px;font-weight:700;line-height:20px}

/* bottom scene */
.landscape{left:0;top:1000px;width:783px;height:160px;
  background:linear-gradient(180deg,#cfe8f7 0,#9fcf7a 30%,var(--grass) 55%,var(--grass-dark) 100%)}
.cta{left:196px;top:1050px;width:390px;height:40px;background:var(--purple);border-radius:8px;
  color:var(--white);font-family:"Lilita One",sans-serif;font-size:17px;text-align:center;line-height:40px;
  box-shadow:0 4px 0 #482670}
.footer{left:0;top:1160px;width:783px;height:40px;background:var(--footer);display:flex;align-items:center;
  justify-content:space-between;padding:0 48px;font-size:7px;color:#c8dcb9}
.footer nav{display:flex;gap:12px}
</style>
</head>
<body>
<div class="page">

  <div class="abs top-links"><span>Home</span><span>About</span><span>Shop</span><span>My Account</span><span>Contact</span></div>
  <div class="abs logo">Logo</div>
  <div class="abs doghouse" role="img" aria-label="Illustration of a red-roofed dog house with a puppy and a bone"></div>
  <div class="abs ribbon">FREE SHIPPING ON ORDERS</div>

  <div class="abs nav">
    <span class="dot"></span>
    <ul><li>DOGS</li><li>CATS</li><li>FISH</li><li>BIRD</li><li>SMALL PET</li><li>CONTACT</li></ul>
    <div class="search"><span>SEARCH</span><span>&#9906;</span></div>
  </div>

  <div class="abs hero-slide" role="img" aria-label="Slider photo of a dog wearing glasses in front of books"></div>
  <div class="abs services">
    <div class="service"><div><h3>PET GROOMING</h3><p>Professional care for happy pets</p></div><span class="go"><svg width="8" height="8" viewBox="0 0 8 8"><path d="M2 1l4 3-4 3" stroke="#fff" stroke-width="1.5" fill="none"/></svg></span></div>
    <div class="service"><div><h3>ADOPT A PET</h3><p>Find a loving friend today</p></div><span class="go"><svg width="8" height="8" viewBox="0 0 8 8"><path d="M2 1l4 3-4 3" stroke="#fff" stroke-width="1.5" fill="none"/></svg></span></div>
    <div class="service"><div><h3>PET SUPPLIES</h3><p>Quality products for every pet</p></div><span class="go"><svg width="8" height="8" viewBox="0 0 8 8"><path d="M2 1l4 3-4 3" stroke="#fff" stroke-width="1.5" fill="none"/></svg></span></div>
  </div>

  <div class="abs main">
    <div class="abs promo promo-food"><h2>PET FOOD STORE</h2><p>We have the finest foods for all pets</p><span class="btn">SHOP NOW</span><span class="thumb" role="img" aria-label="Photo of a pet food bowl"></span></div>
    <div class="abs promo promo-school"><h2>PUPPY SCHOOL</h2><p>Professional puppy training done right</p><span class="btn">READ MORE</span><span class="thumb" role="img" aria-label="Photo of a puppy"></span></div>

    <div class="abs col" style="left:14px">
      <h3>Grooming Service</h3>
      <p>Our gentle groomers give every dog and cat a clean, healthy coat. Book a bath, trim or nail care session and let your pet leave looking and feeling great.</p>
      <span class="more">Read More</span>
    </div>
    <div class="abs col" style="left:270px">
      <h3>Health &amp; Fitness</h3>
      <p>Keep your companion active with balanced meals, daily walks and regular checkups. Our team shares simple tips to help pets stay fit and strong all year.</p>
      <span class="more">Read More</span>
    </div>
    <div class="abs offer"><h3>Special Offers</h3><p>Join our list for weekly deals and new arrivals.</p></div>

    <div class="abs hours">
      <table>
        <tr><td>Monday</td><td>9am - 6pm</td></tr>
        <tr><td>Tuesday</td><td>9am - 6pm</td></tr>
        <tr><td>Wednesday</td><td>9am - 6pm</td></tr>
        <tr><td>Thursday</td><td>9am - 8pm</td></tr>
        <tr><td>Weekend</td><td>10am - 4pm</td></tr>
      </table>
    </div>
    <div class="abs video" role="img" aria-label="Video still of a dog riding a skateboard next to a cat"></div>

    <div class="abs tabs"><span class="on">Latest Products</span><span>Best Selling</span><span>On Sale</span></div>
    <div class="abs products">
      <div class="product"><span class="badge">NEW</span><div class="pic" role="img" aria-label="Dog food bag" style="background:linear-gradient(#c0392b,#7a1f16)"></div><h4>Turkey Beef Formula</h4><div class="stars">★★★★★</div><div class="price">$36.00</div><span class="cart">ADD TO CART</span></div>
      <div class="product"><span class="badge">NEW</span><div class="pic" role="img" aria-label="Dog food bag" style="background:linear-gradient(#f1c232,#c98a12)"></div><h4>Hearthbowl Chicken &amp; Rice</h4><div class="stars">★★★★★</div><div class="price">$34.00</div><span class="cart">ADD TO CART</span></div>
      <div class="product"><div class="pic" role="img" aria-label="Cat food bag" style="background:linear-gradient(#dfe6ee,#8aa0b8)"></div><h4>Meadowvet Indoor Cat</h4><div class="stars">★★★★★</div><div class="price">$29.00</div><span class="cart">ADD TO CART</span></div>
      <div class="product"><div class="pic" role="img" aria-label="Dog food bag" style="background:linear-gradient(#5aa8de,#2b6aa3)"></div><h4>Active Grain Dog Mix</h4><div class="stars">★★★★★</div><div class="price">$31.00</div><span class="cart">ADD TO CART</span></div>
      <div class="product"><div class="pic" role="img" aria-label="Dog food bag" style="background:linear-gradient(#e98a2a,#a8521a)"></div><h4>Farm Harvest Blend</h4><div class="stars">★★★★★</div><div class="price">$27.00</div><span class="cart">ADD TO CART</span></div>
    </div>
  </div>

  <div class="abs landscape" role="img" aria-label="Illustrated grassy hills with rocks, a birdhouse and a small dog"></div>
  <div class="abs cta">Book an Appointment Today!</div>
  <div class="abs footer"><span>Copyright 2015 &copy; Logo</span><nav><span>Home</span><span>Shop</span><span>Blog</span><span>Contact</span></nav></div>

</div>
</body>
</html>
```